Dental Business Card

I need Dental oriented business cards.
On the front side -
- on the first line, my name:
Dr Marlo Vintner
- on the second line (just underneath):
Doctor of Dental Medicine
- on the third line, or underneath that or in a corner, I would like the address and phone number:
5182 Ch. Birchfield
Montreal QC H2T 4B9
514-629-5074
- other than that i would maybe like a logo of a tooth, but i want it to be subtle and very basic!
- I would like the card to be preferably black or dark grey-ish with the writing in white
On the other side -
- 2-3 lines with the possibility to write the next appointment the box with the lines should be white, with the rest of the card being black

```html
<!DOCTYPE html>
<html lang="en">
<head>
<meta charset="utf-8">
<title>Dr Marlo Vintner – Business Card</title>
<link rel="stylesheet" href="https://fonts.googleapis.com/css2?family=Open+Sans:wght@400;600;700&display=swap">
<style>
  :root {
    --canvas-bg: #8e8f92;
    --card-bg: #1a1315;
    --card-bg-deep: #120d0e;
    --mark-tone: #3a3335;
    --text-main: #ffffff;
    --text-soft: #d9d6d7;
    --icon-tone: #8d8789;
    --slot-bg: #ffffff;
  }
  * { box-sizing: border-box; margin: 0; padding: 0; }
  html, body {
    width: 1200px;
    height: 800px;
    overflow: hidden;
  }
  body {
    background: var(--canvas-bg);
    font-family: "Open Sans", Arial, sans-serif;
    position: relative;
  }
  .card {
    position: absolute;
    top: 259px;
    width: 500px;
    height: 282px;
    background: linear-gradient(135deg, var(--card-bg) 0%, var(--card-bg-deep) 100%);
    overflow: hidden;
    box-shadow: 0 6px 18px rgba(0, 0, 0, 0.35);
  }
  .card--back { left: 70px; }
  .card--front { left: 630px; }

  .tooth-mark {
    position: absolute;
    left: 0;
    top: 22px;
    width: 210px;
    height: 240px;
    background: radial-gradient(ellipse at 50% 45%, var(--mark-tone) 0%, rgba(58, 51, 53, 0.35) 45%, rgba(26, 19, 21, 0) 72%);
  }

  /* Back side */
  .appointment-label {
    position: absolute;
    right: 14px;
    top: 118px;
    font-size: 12px;
    font-weight: 400;
    color: var(--text-main);
    letter-spacing: 0.2px;
  }
  .appointment-slot {
    position: absolute;
    left: 56px;
    right: 8px;
    top: 140px;
    height: 108px;
    background: var(--slot-bg);
    border-radius: 10px;
  }

  /* Front side */
  .identity {
    position: absolute;
    left: 284px;
    top: 46px;
    color: var(--text-main);
  }
  .identity__name {
    font-size: 19px;
    font-weight: 700;
    line-height: 1.2;
  }
  .identity__title {
    font-size: 11px;
    font-weight: 400;
    color: var(--text-soft);
    margin-top: 3px;
  }
  .contact {
    position: absolute;
    left: 284px;
    top: 172px;
    list-style: none;
    color: var(--text-soft);
    font-size: 12.5px;
    line-height: 19px;
  }
  .contact__row {
    display: flex;
    align-items: flex-start;
  }
  .contact__icon {
    width: 12px;
    height: 19px;
    margin-right: 8px;
    flex: none;
    display: flex;
    align-items: center;
    justify-content: center;
  }
  .contact__icon svg { width: 11px; height: 11px; fill: var(--icon-tone); }
</style>
</head>
<body>

  <section class="card card--back" aria-label="Appointment card, back side">
    <div class="tooth-mark" role="img" aria-label="Subtle tooth outline decoration"></div>
    <p class="appointment-label">Next Appointment</p>
    <div class="appointment-slot" aria-label="Space to write the next appointment"></div>
  </section>

  <section class="card card--front" aria-label="Business card, front side">
    <div class="tooth-mark" role="img" aria-label="Subtle tooth outline decoration"></div>
    <div class="identity">
      <h1 class="identity__name">Dr Marlo Vintner</h1>
      <p class="identity__title">Doctor of Dental Medicine</p>
    </div>
    <ul class="contact">
      <li class="contact__row">
        <span class="contact__icon">
          <svg viewBox="0 0 12 12" aria-hidden="true"><path d="M6 0.5a3.6 3.6 0 0 0-3.6 3.6C2.4 6.8 6 10 6 10s3.6-3.2 3.6-5.9A3.6 3.6 0 0 0 6 0.5zm0 5a1.4 1.4 0 1 1 0-2.8 1.4 1.4 0 0 1 0 2.8z"/><rect x="1.5" y="10.6" width="9" height="0.9" rx="0.4"/></svg>
        </span>
        <span>5182 Ch. Birchfield<br>Montreal QC H2T 4B9</span>
      </li>
      <li class="contact__row">
        <span class="contact__icon">
          <svg viewBox="0 0 12 12" aria-hidden="true"><path d="M1 4.2C1 2.6 3.2 1.5 6 1.5s5 1.1 5 2.7v0.9H8.6V3.9C8 3.6 7 3.5 6 3.5s-2 .1-2.6.4v1.2H1z"/><path d="M2.4 6h7.2l0.9 4.5H1.5z"/></svg>
        </span>
        <span>514-629-5074</span>
      </li>
    </ul>
  </section>

</body>
</html>
```